Reputable business cards for Diplom Kauffrau, Privat und Geschäftslich

The business cards should be reputable, valuable and elegant in order to be able to use them for business. The design should also include a sophistication that is conspicuous. This could be a picture, an ornament, a sublime print or a kind of logo of the initials of my name "MD". The font should be clear and legible.
Target Market(s)
Business contacts, friends and acquaintances
Contact Information for Business Card
Diplom-Kauffrau Mirela Donat
Lindenhofweg 7 50931 Kerpen
Mobil +49 171 804 29 57
e-mail mirela.donat@postwerk.de
Colors
Designer to choose colors to be used in the design.
Requirements
Must have
- Clear and easy to read font My name in larger font than the other information Visual conspicuity / specificity
Nice to have
- Different colors
Should not have
- Ornate font, playful

```html
<!DOCTYPE html>
<html lang="de">
<head>
<meta charset="utf-8">
<title>Mirela Donat – Visitenkarten</title>
<link rel="stylesheet" href="https://fonts.googleapis.com/css2?family=Cinzel:wght@400;700&family=Lato:wght@300;400&display=swap">
<style>
  :root {
    --backdrop: #4a403b;
    --card: #0e0e0e;
    --card-edge: #1c1c1c;
    --gold: #d9ac2e;
    --silver: #cfcfd2;
    --silver-dim: #9c9ca0;
    --text-soft: #b9b9b9;
    --divider: #2a2a2a;
  }
  * { box-sizing: border-box; margin: 0; padding: 0; }
  html, body { width: 1200px; height: 844px; overflow: hidden; }
  body {
    background: var(--backdrop);
    display: flex;
    align-items: center;
    justify-content: center;
    gap: 60px;
  }
  .card {
    width: 510px;
    height: 292px;
    background: var(--card);
    border: 1px solid var(--card-edge);
    position: relative;
    box-shadow: 0 12px 30px rgba(0,0,0,.45);
  }

  /* Contact side */
  .card--contact { display: flex; }
  .contact-mark {
    width: 230px;
    display: flex;
    align-items: center;
    justify-content: center;
    gap: 14px;
  }
  .contact-mark .mark-dot {
    width: 18px; height: 18px;
    border-radius: 50%;
    background: var(--gold);
  }
  .contact-mark .mark-name {
    font-family: "Cinzel", serif;
    font-weight: 400;
    font-size: 64px;
    color: var(--gold);
    letter-spacing: 2px;
  }
  .contact-divider {
    width: 1px;
    margin: 40px 0;
    background: var(--divider);
  }
  .contact-info {
    padding: 52px 0 0 24px;
    font-family: "Lato", sans-serif;
    color: var(--text-soft);
    font-weight: 300;
  }
  .contact-info .holder-name {
    font-family: "Cinzel", serif;
    font-weight: 700;
    font-size: 19px;
    color: var(--gold);
    letter-spacing: .5px;
  }
  .contact-info .holder-title {
    font-size: 14px;
    margin-bottom: 10px;
  }
  .contact-line {
    display: flex;
    align-items: center;
    gap: 8px;
    font-size: 15px;
    line-height: 1.45;
  }
  .contact-line svg { width: 12px; height: 12px; fill: var(--gold); flex: none; }
  .contact-address {
    margin-top: 12px;
    font-size: 15px;
    line-height: 1.4;
  }

  /* Name side */
  .card--name {
    display: flex;
    flex-direction: column;
    align-items: center;
    justify-content: center;
  }
  .name-mark {
    display: flex;
    align-items: center;
    gap: 12px;
    margin-bottom: 22px;
  }
  .name-mark .mark-dot {
    width: 14px; height: 14px;
    border-radius: 50%;
    background: var(--silver);
  }
  .name-mark .mark-name {
    font-family: "Cinzel", serif;
    font-size: 50px;
    color: var(--silver);
    letter-spacing: 2px;
  }
  .name-holder {
    font-family: "Cinzel", serif;
    font-size: 24px;
    color: var(--silver);
    letter-spacing: 1px;
  }
  .name-title {
    font-family: "Cinzel", serif;
    font-size: 11px;
    color: var(--silver-dim);
    letter-spacing: 2.5px;
    margin-top: 2px;
  }
</style>
</head>
<body>
  <section class="card card--contact">
    <div class="contact-mark">
      <span class="mark-dot"></span>
      <span class="mark-name">MD</span>
    </div>
    <div class="contact-divider"></div>
    <div class="contact-info">
      <p class="holder-name">MIRELA DONAT</p>
      <p class="holder-title">Diplom-Kauffrau</p>
      <p class="contact-line">
        <svg viewBox="0 0 24 24" aria-hidden="true"><path d="M6.6 10.8a15.1 15.1 0 0 0 6.6 6.6l2.2-2.2a1 1 0 0 1 1-.25 11.4 11.4 0 0 0 3.6.57 1 1 0 0 1 1 1V20a1 1 0 0 1-1 1A17 17 0 0 1 3 4a1 1 0 0 1 1-1h3.5a1 1 0 0 1 1 1c0 1.25.2 2.45.57 3.57a1 1 0 0 1-.25 1z"/></svg>
        +49 171 804 29 57
      </p>
      <p class="contact-line">
        <svg viewBox="0 0 24 24" aria-hidden="true"><path d="M2 5h20v14H2z M2 5l10 8 10-8" /></svg>
        mirela.donat@postwerk.de
      </p>
      <p class="contact-address">Lindenhofweg<br>7 50931 Kerpen</p>
    </div>
  </section>

  <section class="card card--name">
    <div class="name-mark">
      <span class="mark-dot"></span>
      <span class="mark-name">MD</span>
    </div>
    <p class="name-holder">MIRELA DONAT</p>
    <p class="name-title">DIPLOM-KAUFFRAU</p>
  </section>
</body>
</html>
```